Rivet Athletic Supply Inc.

Need to create a website that is informational and has the ability to sell goods and services. Such as a custom t shirt designer where the user can upload and image to be displayed on the garmet. The sports we specialize in are basketball, football, and baseball.

Would like like:
Home Page
Locker Room Page:
Custom Uniforms Page
Custom Shirt Creator
Brands
About

Competitor websites are
lornfieldsportsco.example
qtv.example
wmdgear.example

```html
<!DOCTYPE html>
<html lang="en">
<head>
<meta charset="utf-8">
<title>Rivet Athletic Supply</title>
<link href="https://fonts.googleapis.com/css2?family=Jost:wght@400;500&family=Oswald:wght@600;700&display=swap" rel="stylesheet">
<style>
:root{
  --red:#d0413d;
  --blue:#2266bb;
  --ink:#111111;
  --muted:#555555;
  --card:#e6e6e6;
  --black:#000000;
  --white:#ffffff;
}
*{box-sizing:border-box;margin:0;padding:0}
html,body{width:1200px;height:2409px;overflow:hidden}
body{font-family:'Jost',sans-serif;color:var(--ink);background:var(--white);position:relative}
.heading{font-family:'Oswald',sans-serif;font-weight:700;text-transform:uppercase;letter-spacing:.5px}
.slant{clip-path:polygon(0 0,100% 0,calc(100% - 10px) 100%,0 100%)}
.btn{display:inline-flex;align-items:center;justify-content:center;color:var(--white);font-size:19px;text-decoration:none}
.btn-red{background:var(--red)}
.btn-blue{background:var(--blue)}

/* header */
.site-header{position:absolute;top:0;left:0;width:1200px;height:78px;display:flex;align-items:center;padding:0 105px}
.brand{display:flex;align-items:center;gap:8px;font-size:20px;font-weight:500;color:var(--blue);width:190px}
.brand-mark{width:14px;height:14px;background:var(--red)}
.main-nav{display:flex;gap:21px;font-size:14px;text-transform:uppercase}
.main-nav a{color:var(--ink);text-decoration:none}
.main-nav a.active{color:var(--red)}
.header-icons{display:flex;gap:20px;margin-left:auto}
.header-icons svg{width:20px;height:20px}

/* hero */
.hero{position:absolute;top:78px;left:0;width:1200px;height:531px;overflow:hidden}
.hero-bg{position:absolute;inset:0;background:linear-gradient(90deg,#0e0e14 0%,#1c1a20 45%,#3a2a28 70%,#2a2020 100%)}
.hero-player{position:absolute;left:600px;top:0;width:320px;height:531px;background:linear-gradient(180deg,#4a3028,#6a3a2a 50%,#2a1a18)}
.hero-floor{position:absolute;left:0;bottom:0;width:1200px;height:110px;background:linear-gradient(180deg,rgba(90,50,30,0),rgba(120,70,40,.7))}
.hero-copy{position:absolute;left:104px;top:126px;color:var(--white)}
.hero-copy h1{font-family:'Oswald',sans-serif;font-weight:700;font-size:42px;line-height:48px;text-transform:uppercase}
.hero-copy p{font-size:21px;line-height:27px;margin-top:20px;width:500px}
.hero-actions{display:flex;gap:32px;margin-top:28px}
.hero-actions .btn{height:53px;font-size:16px;text-transform:uppercase}

/* categories */
.categories-title{position:absolute;top:682px;width:1200px;text-align:center;color:var(--red);font-size:44px;line-height:52px}
.tabs{position:absolute;top:767px;left:352px;display:flex;gap:20px}
.tab{width:152px;height:48px;border:1px solid var(--ink);display:flex;align-items:center;justify-content:center;font-size:19px}
.tab.active{background:var(--blue);border-color:var(--blue);color:var(--white)}
.sort{position:absolute;top:762px;left:955px;width:140px;display:flex;justify-content:space-between;font-size:18px}
.products{position:absolute;top:860px;left:105px;display:flex;gap:32px}
.product{width:310px;height:383px;display:flex;flex-direction:column}
.product-media{height:196px;display:flex;align-items:center;justify-content:center;background:var(--white)}
.ball{width:128px;height:128px;border-radius:50%;background:radial-gradient(circle at 38% 35%,#f79a55,#e5642a 60%,#b8461c)}
.product-info{flex:1;background:var(--card);display:flex;flex-direction:column;align-items:center;padding-top:22px}
.product-name{font-size:19px}
.price{font-size:19px;margin-top:12px}
.price .now{color:var(--red)}
.price .was{text-decoration:line-through}
.product .btn{width:161px;height:48px;margin-top:22px}
.view-all{position:absolute;top:1284px;left:507px;width:169px;height:51px;border:1px solid var(--ink);display:flex;align-items:center;justify-content:center;font-size:19px;color:var(--ink);text-decoration:none}

/* about */
.about-media{position:absolute;top:1417px;left:105px;width:452px;height:362px}
.about-photo{position:absolute;top:0;height:362px}
.about-photo.one{left:0;width:201px;clip-path:polygon(28px 0,100% 0,calc(100% - 28px) 100%,0 100%);background:linear-gradient(160deg,#2a3040,#c98a58 60%,#d9a06a)}
.about-photo.two{left:188px;width:264px;clip-path:polygon(28px 0,100% 0,calc(100% - 28px) 100%,0 100%);background:linear-gradient(170deg,#1a2638,#34486a 55%,#1e3a22)}
.about-copy{position:absolute;top:1414px;left:607px;width:480px}
.eyebrow{color:var(--blue);font-size:20px;text-transform:uppercase}
.about-copy h2{color:var(--red);font-size:42px;line-height:50px}
.about-copy p{color:var(--muted);font-size:16px;line-height:29px;margin-top:18px}
.about-copy .btn{width:161px;height:48px;margin-top:30px}

/* vendors */
.vendors-title{position:absolute;top:1851px;width:1200px;text-align:center;color:var(--red);font-size:44px;line-height:52px}
.vendor-row{position:absolute;top:1950px;left:104px;width:992px;height:40px;display:flex;align-items:center;justify-content:space-between}
.arrow{width:35px;height:35px;border-radius:50%;display:flex;align-items:center;justify-content:center}
.arrow.prev{background:#dddddd}
.arrow.next{background:var(--blue)}
.vendor{font-size:19px;font-weight:500;color:#333333;width:110px;text-align:center}

/* footer */
.site-footer{position:absolute;top:2041px;left:0;width:1200px;height:333px;background:var(--black);color:var(--white)}
.footer-brand{position:absolute;top:48px;width:1200px;display:flex;justify-content:center;align-items:center;gap:12px;font-size:40px;font-weight:500;color:var(--blue)}
.footer-brand .brand-mark{width:28px;height:28px}
.footer-nav{position:absolute;top:141px;width:1200px;display:flex;justify-content:center;gap:21px;font-size:14px;text-transform:uppercase}
.contact{position:absolute;top:182px;width:1200px;display:flex;justify-content:center;gap:32px;font-size:22px}
.contact-item{display:flex;align-items:center;gap:12px}
.contact-icon{width:44px;height:44px;border-radius:50%;background:var(--red);display:flex;align-items:center;justify-content:center}
.social{position:absolute;top:265px;width:1200px;display:flex;justify-content:center;gap:19px}
.social span{width:34px;height:34px;border:3px solid var(--white);border-radius:8px}
.copyright{position:absolute;top:2374px;left:0;width:1200px;height:35px;background:var(--blue);color:var(--white);display:flex;align-items:center;justify-content:center;font-size:16px}
</style>
</head>
<body>

<header class="site-header">
  <div class="brand"><span class="brand-mark"></span>Rivet Athletic</div>
  <nav class="main-nav">
    <a class="active" href="#">Home</a>
    <a href="#">About Us</a>
    <a href="#">Locker Room</a>
    <a href="#">Custom Uniforms</a>
    <a href="#">Custom Shirt Creator</a>
    <a href="#">Brands</a>
  </nav>
  <div class="header-icons">
    <svg viewBox="0 0 20 20" fill="none" stroke="#111" stroke-width="1.6"><circle cx="8.5" cy="8.5" r="6"/><path d="M13 13l5 5"/></svg>
    <svg viewBox="0 0 20 20" fill="none" stroke="#111" stroke-width="1.6"><circle cx="10" cy="7" r="3.5"/><path d="M3.5 18c1-4 4-5.5 6.5-5.5s5.5 1.5 6.5 5.5"/></svg>
    <svg viewBox="0 0 20 20" fill="none" stroke="#111" stroke-width="1.6"><path d="M2 3h3l2 10h9l2-7H6"/><circle cx="8" cy="17" r="1.3"/><circle cx="15" cy="17" r="1.3"/></svg>
  </div>
</header>

<section class="hero">
  <div class="hero-bg" role="img" aria-label="Dim brick-walled gym with warm wooden floor"></div>
  <div class="hero-player" role="img" aria-label="Basketball player in a navy and orange jersey dribbling a ball"></div>
  <div class="hero-floor"></div>
  <div class="hero-copy">
    <h1>Your Team<br>Your Design. Your Game.</h1>
    <p>Professional-grade custom uniforms for Basketball Football, and Baseball. Upload your logo and see it live.</p>
    <div class="hero-actions">
      <a class="btn btn-red slant" style="width:237px" href="#">Start Designing Now</a>
      <a class="btn btn-blue slant" style="width:164px" href="#">View Gallery</a>
    </div>
  </div>
</section>

<h2 class="categories-title heading">Sports Categories</h2>
<div class="tabs">
  <div class="tab active">Basketball</div>
  <div class="tab">Football</div>
  <div class="tab">Baseball</div>
</div>
<div class="sort"><span>Featured</span><svg width="14" height="14" viewBox="0 0 14 14" fill="none" stroke="#111" stroke-width="1.6"><path d="M2 4l5 5 5-5"/></svg></div>

<div class="products">
  <article class="product">
    <div class="product-media"><div class="ball" role="img" aria-label="Orange basketball"></div></div>
    <div class="product-info">
      <div class="product-name">Courtline Autograph Basketball</div>
      <div class="price"><span class="now">$30.00</span> <span class="was">$35.00</span></div>
      <a class="btn btn-red slant" href="#">Shop Now</a>
    </div>
  </article>
  <article class="product">
    <div class="product-media"><div class="ball" role="img" aria-label="Orange basketball"></div></div>
    <div class="product-info">
      <div class="product-name">Baseline Autograph Basketball</div>
      <div class="price"><span class="now">$30.00</span> <span class="was">$35.00</span></div>
      <a class="btn btn-blue slant" href="#">Shop Now</a>
    </div>
  </article>
  <article class="product" style="margin-left:-4px">
    <div class="product-media"><div class="ball" role="img" aria-label="Orange basketball"></div></div>
    <div class="product-info">
      <div class="product-name">Baseline Autograph Basketball</div>
      <div class="price"><span class="now">$30.00</span> <span class="was">$35.00</span></div>
      <a class="btn btn-blue slant" href="#">Shop Now</a>
    </div>
  </article>
</div>
<a class="view-all" href="#">View All</a>

<div class="about-media">
  <div class="about-photo one" role="img" aria-label="Baseball batter mid-swing kicking up dirt"></div>
  <div class="about-photo two" role="img" aria-label="Football player in striped kit running with the ball"></div>
</div>
<div class="about-copy">
  <div class="eyebrow">About Us</div>
  <h2 class="heading">What We Do</h2>
  <p>is simply dummy text of the printing and typesetting industry. Lorem Ipsum has been the industry's standard dummy text ever since the 1500s, when an unknown printer took a galley of type and scrambled it to make a type specimen book. It has survived not only five centuries, but also the leap into electronic typesetting, remaining essentially unchanged.</p>
  <a class="btn btn-blue slant" href="#">Know more</a>
</div>

<h2 class="vendors-title heading">Our Vendor Catalogs</h2>
<div class="vendor-row">
  <span class="arrow prev"><svg width="16" height="16" viewBox="0 0 16 16" fill="none" stroke="#111" stroke-width="2"><path d="M10 2L4 8l6 6"/></svg></span>
  <span class="vendor">Velkora</span>
  <span class="vendor">Ironvale</span>
  <span class="vendor">Helmcraft</span>
  <span class="vendor">Pitchline</span>
  <span class="vendor">Wyndell</span>
  <span class="vendor">Motivo</span>
  <span class="vendor">Rowanly</span>
  <span class="arrow next"><svg width="16" height="16" viewBox="0 0 16 16" fill="none" stroke="#fff" stroke-width="2"><path d="M6 2l6 6-6 6"/></svg></span>
</div>

<footer class="site-footer">
  <div class="footer-brand"><span class="brand-mark"></span>Rivet Athletic Supply</div>
  <nav class="footer-nav">
    <span>Home</span><span>About Us</span><span>Locker Room</span><span>Custom Uniforms</span><span>Custom Shirt Creator</span><span>Brands</span>
  </nav>
  <div class="contact">
    <div class="contact-item">
      <span class="contact-icon"><svg width="22" height="22" viewBox="0 0 24 24" fill="#fff"><path d="M6.6 10.8a15.1 15.1 0 006.6 6.6l2.2-2.2a1 1 0 011-.25 11.4 11.4 0 003.6.57 1 1 0 011 1V20a1 1 0 01-1 1A17 17 0 013 4a1 1 0 011-1h3.5a1 1 0 011 1c0 1.25.2 2.45.57 3.57a1 1 0 01-.25 1z"/></svg></span>
      <span>5550147283</span>
    </div>
    <div class="contact-item">
      <span class="contact-icon"><svg width="22" height="22" viewBox="0 0 24 24" fill="none" stroke="#fff" stroke-width="1.8"><rect x="3" y="5" width="18" height="14" rx="2"/><path d="M3 7l9 6 9-6"/></svg></span>
      <span>info@rivetathletic.example</span>
    </div>
  </div>
  <div class="social" aria-label="Social links"><span></span><span></span><span></span></div>
</footer>
<div class="copyright">© 2025 Rivet Athletic Supply | All Rights Reserved</div>

</body>
</html>
```